New Business Cards for Torvin Group

We need a new Business Card to compliment our new logo. We are a vibrant design, manufacture and install business providing recreation areas, public parks and Municipal spaces. We want business cards that are classy, modern and clean.

We have recently changed our logo, and are celebrating our 40th anniversary. We want business cards with a new modern design to reflect our status.

Target Market(s)

Customers

Contact Information for Business Card

We need all the details of our 3 offices as per the business card attached. Please disregard the old logo on the business card, the other three files show our new logo.

Requirements
Must have
• All info as per attached business card but with new logo.
Nice to have

```html
<!DOCTYPE html>
<html lang="en">
<head>
<meta charset="utf-8">
<title>Torvin Group Business Card</title>
<link href="https://fonts.googleapis.com/css2?family=Lato:wght@400;700&display=swap" rel="stylesheet">
<style>
  :root {
    --backdrop: #2a2a2c;
    --card: #ffffff;
    --band: #4a4a4d;
    --red: #e5262c;
    --ink: #3d3d40;
    --muted: #6c6c70;
    --rule: #cfcfd2;
    --band-rule: #8a8a8e;
  }
  * { margin: 0; padding: 0; box-sizing: border-box; }
  html, body { width: 1200px; height: 895px; overflow: hidden; }
  body {
    background: var(--backdrop);
    font-family: "Lato", sans-serif;
    position: relative;
  }
  .card {
    position: absolute;
    left: 100px; top: 162px;
    width: 1000px; height: 571px;
    background: var(--card);
    box-shadow: 0 10px 30px rgba(0,0,0,.5);
  }
  .brand { position: absolute; left: 150px; top: 110px; display: flex; align-items: center; gap: 22px; }
  .brand-dot { width: 130px; height: 130px; border-radius: 50%; background: var(--red); flex: none; }
  .brand-text { display: flex; flex-direction: column; }
  .brand-name { font-size: 40px; font-weight: 700; color: var(--ink); letter-spacing: 1px; line-height: 1; }
  .brand-est { font-size: 20px; color: var(--muted); margin-top: 10px; align-self: flex-end; }
  .divider { position: absolute; left: 560px; top: 55px; width: 1px; height: 210px; background: var(--rule); }
  .person { position: absolute; left: 600px; top: 62px; }
  .person-name { font-size: 44px; color: var(--red); font-weight: 400; line-height: 1.05; }
  .person-title { font-size: 19px; color: var(--ink); margin-top: 2px; }
  .person-contacts { margin-top: 28px; font-size: 17px; color: var(--ink); }
  .contact-row { display: flex; align-items: center; gap: 12px; margin-bottom: 6px; }
  .contact-row svg { width: 16px; height: 16px; fill: var(--red); flex: none; }
  .band {
    position: absolute; left: 0; top: 300px; width: 100%; height: 152px;
    background: var(--band);
    border-top: 3px solid var(--red);
    display: flex; align-items: center; padding: 0 40px;
  }
  .office { flex: 1; padding: 0 28px; color: #fff; font-size: 17px; line-height: 1.35; }
  .office + .office { border-left: 1px solid var(--band-rule); }
  .office-title { color: var(--red); font-weight: 700; font-size: 18px; margin-bottom: 2px; }
  .footer {
    position: absolute; left: 0; top: 490px; width: 100%;
    text-align: center; font-size: 19px; color: var(--ink);
  }
  .footer .label { color: var(--red); }
  .footer .sep { color: var(--muted); margin: 0 14px; }
</style>
</head>
<body>
  <main class="card">
    <div class="brand">
      <div class="brand-dot"></div>
      <div class="brand-text">
        <span class="brand-name">Torvin Group</span>
        <span class="brand-est">Est. 1979</span>
      </div>
    </div>

    <div class="divider"></div>

    <section class="person">
      <h1 class="person-name">Rami Nasser</h1>
      <p class="person-title">Managing Partner</p>
      <div class="person-contacts">
        <div class="contact-row">
          <svg viewBox="0 0 24 24" aria-hidden="true"><path d="M6.6 10.8a15.1 15.1 0 0 0 6.6 6.6l2.2-2.2c.3-.3.7-.4 1-.2 1.1.4 2.3.6 3.6.6.6 0 1 .4 1 1V20c0 .6-.4 1-1 1A17 17 0 0 1 3 4c0-.6.4-1 1-1h3.5c.6 0 1 .4 1 1 0 1.3.2 2.5.6 3.6.1.3 0 .7-.2 1z"/></svg>
          <span>+971 (0)50 555 0142</span>
        </div>
        <div class="contact-row">
          <svg viewBox="0 0 24 24" aria-hidden="true"><path d="M2 5h20v14H2zM2 6l10 7 10-7v-1H2z" /></svg>
          <span>rami@torvingroup.com</span>
        </div>
      </div>
    </section>

    <section class="band">
      <div class="office">
        <p class="office-title">Head Office</p>
        <p>10482 Abu Dhabi, U.A.E.</p>
        <p>Tel: +971 (0)2 555 0184</p>
        <p>Fax: +971 (0)2 555 0183</p>
      </div>
      <div class="office">
        <p class="office-title">Dubai Office</p>
        <p>207314 Dubai, U.A.E.</p>
        <p>Tel: +971 (0)4 555 0191</p>
        <p>Fax: +971 (0)4 555 0169</p>
      </div>
      <div class="office">
        <p class="office-title">Qatar Office</p>
        <p>3028 Doha, Qatar</p>
        <p>Tel: +974 5550 0195</p>
        <p>Fax: +974 5550 0160</p>
      </div>
    </section>

    <p class="footer">
      <span class="label">Email:</span> sales@torvingroup.com
      <span class="sep">|</span>
      <span class="label">Web:</span> www.torvingroup.com
    </p>
  </main>
</body>
</html>
```